Income Tax Flyer - Updates Needed

Just need to update this flyer design and give it a new look. We would like to keep all the same wording but make it stand out a little more. Our selling point is the "Same Day Tax Advance up to $6,000"

Industry/Entity Type

Lending, Small Loans, Tax Services, Title Loans, Personal Loans

```html
<!DOCTYPE html>
<html lang="en">
<head>
<meta charset="utf-8">
<title>Tax Advance Flyer</title>
<link href="https://fonts.googleapis.com/css2?family=Outfit:wght@400;500;600;700&display=swap" rel="stylesheet">
<style>
  :root {
    --backdrop: #1b1b1b;
    --paper: #ffffff;
    --brand-red: #c40202;
    --brand-green: #105308;
    --ink: #111111;
    --photo-light: #9a9a9a;
    --photo-dark: #1a1a1a;
  }
  * { margin: 0; padding: 0; box-sizing: border-box; }
  html, body {
    width: 1056px; height: 1200px; overflow: hidden;
    background: var(--backdrop);
    font-family: "Outfit", sans-serif;
  }
  .flyer {
    position: absolute; left: 157px; top: 30px;
    width: 742px; height: 1141px;
    background: var(--paper);
    overflow: hidden;
  }
  .brand {
    position: absolute; left: 36px; top: 70px; width: 240px;
    display: flex; align-items: center; justify-content: center; gap: 10px;
    color: var(--brand-green); font-weight: 700; font-size: 25px; line-height: 1.05;
    text-align: left;
  }
  .brand-mark {
    width: 14px; height: 14px; border-radius: 50%;
    background: var(--brand-red); flex: none;
  }
  .hero-photo {
    position: absolute; left: 280px; top: 0; width: 426px; height: 740px;
    background: linear-gradient(160deg, var(--photo-light) 0%, #6d6d6d 35%, #4a4a4a 65%, var(--photo-dark) 100%);
  }
  .hero-photo-tagline {
    position: absolute; left: 422px; top: 546px;
    color: #fff; font-weight: 600; font-size: 35px; line-height: 43px;
    white-space: nowrap;
  }
  .offer-box {
    position: absolute; left: 36px; top: 338px; width: 347px; height: 283px;
    background: var(--brand-red);
  }
  .offer-tail { position: absolute; left: 342px; top: 620px; }
  .offer-text {
    position: absolute; left: 23px; top: 54px; color: #fff; font-weight: 700;
    white-space: nowrap;
  }
  .offer-lead { font-size: 37px; line-height: 42px; letter-spacing: -0.6px; }
  .offer-amount { font-size: 42px; line-height: 58px; letter-spacing: -0.5px; }
  .offer-when { font-size: 44px; line-height: 56px; }
  .offer-rule {
    position: absolute; left: 27px; top: 221px; width: 160px; height: 7px;
    background: var(--brand-green);
  }
  .features {
    position: absolute; left: 0; top: 786px; width: 742px; height: 100px;
  }
  .feature { position: absolute; top: 0; display: flex; gap: 12px; }
  .feature-label {
    font-weight: 600; font-size: 17px; line-height: 24px; color: var(--ink);
    padding-top: 2px; white-space: nowrap;
  }
  .feature-divider {
    position: absolute; top: 4px; width: 2px; height: 76px; background: var(--ink);
  }
  .contact-band {
    position: absolute; left: 0; top: 910px; width: 507px; height: 67px;
    background: var(--brand-green);
    color: #fff; font-weight: 600; font-size: 22px;
    display: flex; align-items: center; padding-left: 45px;
  }
  .locations {
    position: absolute; left: 40px; top: 1010px; list-style: none;
  }
  .locations li {
    display: flex; align-items: center; gap: 16px;
    font-size: 14.5px; letter-spacing: 0.6px; line-height: 24.5px; color: var(--ink);
    white-space: nowrap;
  }
  .contact-divider {
    position: absolute; left: 504px; top: 1015px; width: 2px; height: 63px;
    background: var(--brand-red);
  }
  .phone {
    position: absolute; left: 555px; top: 1030px;
    color: var(--brand-red); font-weight: 600; font-size: 18.5px;
  }
</style>
</head>
<body>
<main class="flyer">
  <div class="brand"><span class="brand-mark"></span><span>Northfield<br>Lending Group</span></div>

  <div class="hero-photo" role="img" aria-label="Black and white photo of a couple working on taxes at a laptop at home"></div>
  <p class="hero-photo-tagline">File your taxes<br>and apply for an<br>Easy Advance!</p>

  <div class="offer-box">
    <div class="offer-text">
      <p class="offer-lead">APPLY HERE FOR</p>
      <p class="offer-amount">$5,000-$6,000</p>
      <p class="offer-when">TODAY!</p>
    </div>
    <div class="offer-rule"></div>
  </div>
  <svg class="offer-tail" width="42" height="44" viewBox="0 0 42 44"><polygon points="0,0 41,0 41,43" fill="#c40202"/></svg>

  <section class="features">
    <div class="feature" style="left:35px">
      <svg width="78" height="78" viewBox="0 0 78 78" fill="none" stroke="#105308" stroke-width="2.2">
        <circle cx="32" cy="32" r="30" stroke-dasharray="3 5"/>
        <line x1="32" y1="10" x2="32" y2="32"/><line x1="32" y1="32" x2="42" y2="42"/>
        <rect x="25" y="48" width="50" height="26" rx="2" fill="#fff"/>
        <text x="50" y="67" font-family="Outfit, sans-serif" font-size="16" font-weight="700" fill="#105308" stroke="none" text-anchor="middle">$</text>
        <circle cx="35" cy="61" r="3"/><circle cx="65" cy="61" r="3"/>
      </svg>
      <p class="feature-label">Available in<br>24 Hours or less</p>
    </div>
    <div class="feature-divider" style="left:267px"></div>
    <div class="feature" style="left:285px">
      <svg width="88" height="92" viewBox="0 0 88 92" fill="none" stroke="#105308" stroke-width="2.2">
        <circle cx="30" cy="30" r="29"/>
        <text x="30" y="40" font-family="Outfit, sans-serif" font-size="30" font-weight="600" fill="#105308" stroke="none" text-anchor="middle">$</text>
        <path d="M44 44 L58 60 L72 58 L78 76 L66 90 L52 88 L38 74 L44 70 L50 74 L42 50 Z" fill="#fff" stroke-linejoin="round"/>
      </svg>
      <p class="feature-label" style="margin-left:-12px">Choose Your<br>Loan Amount</p>
    </div>
    <div class="feature-divider" style="left:506px"></div>
    <div class="feature" style="left:524px">
      <svg width="90" height="70" viewBox="0 0 90 70" fill="none" stroke="#105308" stroke-width="2.2">
        <circle cx="56" cy="32" r="30"/><circle cx="56" cy="32" r="22"/>
        <text x="56" y="43" font-family="Outfit, sans-serif" font-size="30" font-weight="600" fill="#105308" stroke="none" text-anchor="middle">$</text>
        <line x1="10" y1="12" x2="34" y2="12"/><line x1="2" y1="24" x2="28" y2="24"/>
        <line x1="6" y1="40" x2="28" y2="40"/><line x1="12" y1="52" x2="34" y2="52"/>
      </svg>
      <p class="feature-label">Quick and<br>Easy</p>
    </div>
  </section>

  <div class="contact-band">Contact Us Today!</div>

  <ul class="locations">
    <li><svg width="14" height="18" viewBox="0 0 14 18"><path d="M7 0C3 0 0 3 0 7c0 5 7 11 7 11s7-6 7-11c0-4-3-7-7-7z" fill="#111"/><circle cx="7" cy="7" r="2.6" fill="#fff"/></svg>Suite 210 48 Cedar Row, Millbrook, AZ 85001</li>
    <li><svg width="14" height="18" viewBox="0 0 14 18"><path d="M7 0C3 0 0 3 0 7c0 5 7 11 7 11s7-6 7-11c0-4-3-7-7-7z" fill="#111"/><circle cx="7" cy="7" r="2.6" fill="#fff"/></svg>Suite 105 912 Harbor Lane, Eastport, ME 04101</li>
    <li><svg width="14" height="18" viewBox="0 0 14 18"><path d="M7 0C3 0 0 3 0 7c0 5 7 11 7 11s7-6 7-11c0-4-3-7-7-7z" fill="#111"/><circle cx="7" cy="7" r="2.6" fill="#fff"/></svg>2270 Ridgeview Road, Pine Falls, WA 98001</li>
  </ul>
  <div class="contact-divider"></div>
  <p class="phone">Phone Number</p>
</main>
</body>
</html>
```